HMC Business Card Design

We need a business card design for a new company called ' Harbour Mill Coffee'. We are a mobile Coffee Trailer providing Espresso Coffee, Specialty Tea's, Milkshakes, Iced Coffee & Iced Chocolate, Soft drinks and Gourmet Cookies to Sporting Events, Fetes, Animal Shows etc...
We would like Darren's name and mobile phone number on the card along with the harbour mill email address and a link to our facebook page Harbour Mill Coffee.
Can you please attach the Harbour Mill Logo to the business card.
I have tried to attach our logo and a picture of our mobile trailer to give you an idea of how we would like the design similar to the trailer if possible. If these pictures and logo's are not attached please email me and i will send them through.

Contact Information for Business Card

Darren Wilkes
0491 372 806
harbourmillcoffee@mailbox-demo.net
FB Harbour Mill Coffee

Requirements
Must have
• We would like coffee beans in the back ground of the card.

```html
<!DOCTYPE html>
<html lang="en">
<head>
<meta charset="utf-8">
<title>Harbour Mill Coffee – Business Card</title>
<link rel="stylesheet" href="https://fonts.googleapis.com/css2?family=Inconsolata:wght@400;500&display=swap">
<style>
  :root {
    --backdrop: #eceeef;
    --card-white: #fbfaf7;
    --maroon: #6b1f1a;
    --ink: #6a2b22;
    --band-grey: #cfc8c4;
    --bean-light: #a35a2f;
    --bean-mid: #7a3d1f;
    --bean-dark: #3e1d10;
    --wood: #d9b07a;
  }
  html, body {
    margin: 0;
    width: 1200px;
    height: 1200px;
    overflow: hidden;
    background: var(--backdrop);
  }
  .canvas {
    position: relative;
    width: 1200px;
    height: 1200px;
  }
  .card {
    position: absolute;
    left: 160px;
    width: 880px;
    height: 503px;
    border-radius: 28px;
    overflow: hidden;
    box-shadow: 0 6px 18px rgba(0,0,0,0.12);
    background: var(--card-white);
  }
  .card--front { top: 60px; }
  .card--back { top: 637px; }
  .card svg { display: block; }
  .card-text {
    font-family: "Inconsolata", monospace;
    fill: var(--ink);
    white-space: pre;
  }
  .brand-name { font-size: 36px; font-weight: 500; fill: var(--maroon); }
  .brand-name--small { font-size: 24px; }
  .contact-name { font-size: 28px; }
  .contact-line { font-size: 18px; }
  .contact-url { font-size: 16px; }
</style>
</head>
<body>
<main class="canvas">

  <section class="card card--front">
    <svg width="880" height="503" viewBox="0 0 880 503">
      <defs>
        <radialGradient id="beans-front" cx="45%" cy="35%" r="75%">
          <stop offset="0" stop-color="var(--bean-light)"/>
          <stop offset="0.55" stop-color="var(--bean-mid)"/>
          <stop offset="1" stop-color="var(--bean-dark)"/>
        </radialGradient>
        <linearGradient id="wood-front" x1="0" y1="0" x2="1" y2="1">
          <stop offset="0" stop-color="var(--wood)" stop-opacity="0"/>
          <stop offset="1" stop-color="var(--wood)" stop-opacity="0.55"/>
        </linearGradient>
      </defs>
      <g role="img" aria-label="Photograph of roasted coffee beans on a wooden board">
        <rect width="880" height="503" fill="url(#beans-front)"/>
        <rect x="0" y="260" width="320" height="243" fill="url(#wood-front)"/>
      </g>
      <path class="brand-area-border" d="M 260 503 Q 320 170 880 140 L 880 503 Z" fill="var(--maroon)"/>
      <path class="brand-area-band" d="M 282 503 Q 340 190 880 160 L 880 503 Z" fill="var(--band-grey)"/>
      <path class="brand-area" d="M 296 503 Q 352 204 880 174 L 880 503 Z" fill="var(--card-white)"/>
      <circle cx="428" cy="358" r="12" fill="var(--maroon)"/>
      <text class="card-text brand-name" x="452" y="370">Harbour Mill Coffee</text>
    </svg>
  </section>

  <section class="card card--back">
    <svg width="880" height="503" viewBox="0 0 880 503">
      <defs>
        <radialGradient id="beans-back" cx="30%" cy="40%" r="80%">
          <stop offset="0" stop-color="var(--bean-light)"/>
          <stop offset="0.5" stop-color="var(--bean-mid)"/>
          <stop offset="1" stop-color="var(--bean-dark)"/>
        </radialGradient>
      </defs>
      <rect role="img" aria-label="Photograph of roasted coffee beans" width="880" height="503" fill="url(#beans-back)"/>
      <polygon class="info-band" points="250,0 760,0 620,503 250,503" fill="var(--card-white)"/>
      <polygon class="info-stripe" points="772,0 790,0 650,503 632,503" fill="var(--maroon)"/>
      <rect class="info-edge" x="248" y="0" width="4" height="503" fill="var(--maroon)"/>

      <text class="card-text contact-name" x="290" y="92">Darren Wilkes  0491 372 806</text>
      <text class="card-text contact-name" x="290" y="136">Mara Olsen     0492 815 347</text>

      <g class="icon-mail" transform="translate(292,186)">
        <rect width="20" height="14" rx="2" fill="var(--ink)"/>
        <path d="M1 1 L10 8 L19 1" fill="none" stroke="var(--card-white)" stroke-width="1.6"/>
      </g>
      <text class="card-text contact-line" x="320" y="199">harbourmillcoffee@mailbox-demo.net</text>

      <rect class="icon-social" x="294" y="220" width="16" height="16" rx="2" fill="var(--ink)"/>
      <text class="card-text contact-url" x="320" y="234">www.social-demo.net/harbour-mill-coffee</text>

      <g class="brand-box">
        <rect x="60" y="300" width="230" height="160" fill="var(--card-white)"/>
        <rect x="70" y="310" width="210" height="140" fill="none" stroke="var(--maroon)" stroke-width="2"/>
        <text class="card-text brand-name brand-name--small" x="175" y="372" text-anchor="middle">Harbour Mill</text>
        <text class="card-text brand-name brand-name--small" x="175" y="402" text-anchor="middle">Coffee</text>
      </g>
    </svg>
  </section>

</main>
</body>
</html>
```